Start up in business consultancy needs a business card

We need the business card's layout (we have already the logo). Our business is concerned on consultancy services delivered to companies on the matter of sustainability. Business card should be enough essentials and professional style.

Side A with the following info:
logo + a space for the claim (still to identify) + website of the company

Side B with the following info:
Name of business card holder + title of the business card holder + address of the company + space for mobile number, phone number, fax number + e-mail of business card holder + graphic details around.

Target Market(s)

Business of any sector

Industry/Entity Type

Business Service

Contact Information for Business Card

Name of the company:
Pianoverde srl
Società Benefit

Address of the company:
Via Lucerna, 7
21047 - Saronno (VA)

Website:
www.pianoverde.it

Name of the BC' holder:
Luca Ferentino

Title:
Co-fondatore

Email:
luca@pianoverde.it

Mobile:
+39 348 915 2074
Phone:
+39 348 915 2074
Fax:
+39 348 915 2074

Font styles to use
Other font styles liked:
• new gothic

```html
<!DOCTYPE html>
<html lang="it">
<head>
<meta charset="utf-8">
<title>Pianoverde – Stationery</title>
<link rel="stylesheet" href="https://fonts.googleapis.com/css2?family=Work+Sans:wght@400;600&display=swap">
<style>
  :root {
    --bg: #d3d3d5;
    --paper: #f1f1f1;
    --blue: #3762a4;
    --ink-blue: #1f5aa6;
    --stripe-grey: #9a9a9a;
    --text: #3a3a3a;
    --white: #ffffff;
  }
  * { box-sizing: border-box; margin: 0; padding: 0; }
  html, body { width: 1200px; height: 991px; overflow: hidden; }
  body {
    background: var(--bg);
    font-family: "Work Sans", Arial, sans-serif;
    color: var(--text);
    position: relative;
  }
  .piece { position: absolute; overflow: hidden; }
  .paper { background: var(--paper); }
  .blue-fill { background: var(--blue); }

  /* brand lockup */
  .brand { position: absolute; display: flex; align-items: center; font-weight: 400; color: var(--ink-blue); }
  .brand .dot { border: 1.5px solid currentColor; border-radius: 50%; flex: none; }
  .brand.light { color: var(--white); }

  .stripe { position: absolute; left: 0; bottom: 0; width: 100%; display: block; }

  /* letterhead */
  .letterhead { left: 71px; top: 103px; width: 398px; height: 562px; }
  .letterhead .brand { left: 33px; top: 27px; font-size: 12.5px; gap: 6px; }
  .letterhead .brand .dot { width: 35px; height: 35px; }
  .contact-block { position: absolute; border-left: 1px solid #bbb; padding-left: 5px; font-size: 4.6px; line-height: 1.45; }
  .contact-block .company { color: var(--ink-blue); font-weight: 600; }
  .contact-block .gap { height: 4px; }
  .letterhead .contact-block { left: 306px; top: 26px; }
  .letter-body { position: absolute; left: 33px; top: 127px; width: 334px; font-size: 5.3px; line-height: 1.35; }
  .letter-body p { margin-bottom: 7px; }
  .letter-body .address { margin: 9px 0 40px; }
  .sign-row { display: flex; gap: 8px; align-items: flex-start; }
  .signature { width: 62px; height: 34px; background: #f7f7f9; margin-top: -7px; }

  /* folder */
  .folder { left: 507px; top: 90px; width: 434px; height: 575px; border-radius: 3px; }
  .folder .spine { position: absolute; left: 0; top: 0; width: 27px; height: 100%; border-right: 1px solid #2e5591; }
  .folder .brand { left: 191px; top: 77px; font-size: 17px; gap: 8px; }
  .folder .brand .dot { width: 55px; height: 55px; border-width: 2px; }
  .folder .site { position: absolute; right: 60px; bottom: 37px; font-size: 7.5px; color: var(--white); }

  /* business cards */
  .card-front { left: 66px; top: 696px; width: 171px; height: 92px; }
  .holder { position: absolute; left: 11px; top: 24px; }
  .holder .name { font-size: 5.4px; font-weight: 600; color: var(--ink-blue); }
  .holder .role { font-size: 3.6px; margin-top: 2px; }
  .card-front .brand { left: 88px; top: 15px; font-size: 7.5px; gap: 4px; }
  .card-front .brand .dot { width: 21px; height: 21px; }
  .card-contacts { position: absolute; left: 11px; top: 63px; font-size: 3.6px; line-height: 1.45; }
  .card-contacts li { list-style: none; display: flex; align-items: center; gap: 3px; }
  .card-contacts svg { width: 4px; height: 4px; fill: var(--ink-blue); }
  .card-company { position: absolute; right: 11px; top: 69px; font-size: 3.6px; line-height: 1.4; text-align: right; }
  .card-company .company { color: var(--ink-blue); font-weight: 600; }

  .card-back { left: 66px; top: 810px; width: 171px; height: 94px; }
  .card-back .brand { left: 41px; top: 34px; font-size: 8.5px; gap: 5px; }
  .card-back .brand .dot { width: 27px; height: 27px; }
  .card-back .site { position: absolute; width: 100%; top: 78px; text-align: center; font-size: 3.6px; color: var(--white); }

  /* compliment slip */
  .slip { left: 266px; top: 696px; width: 415px; height: 208px; }
  .slip .brand { left: 22px; top: 18px; font-size: 10.5px; gap: 5px; }
  .slip .brand .dot { width: 31px; height: 31px; }
  .slip .contact-block { left: 27px; top: 174px; }

  /* envelope */
  .envelope { left: 718px; top: 696px; width: 415px; height: 208px; }
  .envelope .flap { position: absolute; left: 0; top: 0; width: 415px; height: 59px; }
  .envelope .brand { left: 196px; top: 16px; }
  .envelope .brand .dot { width: 23px; height: 23px; color: var(--white); }
  .envelope .site { position: absolute; width: 100%; top: 184px; text-align: center; font-size: 4.6px; }
</style>
</head>
<body>

  <!-- Letterhead -->
  <section class="piece paper letterhead">
    <div class="brand"><span class="dot"></span><span>pianoverde</span></div>
    <div class="contact-block">
      <div class="company">PIANOVERDE SRL</div>
      <div>Via Lucerna, 7</div>
      <div>21047 - Saronno (VA)</div>
      <div class="gap"></div>
      <div>+39 348 915 2074</div>
      <div>info@pianoverde.it</div>
      <div>www.pianoverde.it</div>
    </div>
    <div class="letter-body">
      <p>30.09.2017</p>
      <p class="address">Recipient's name<br>Lindenweg 4<br>10115 Berlin<br>Germany</p>
      <p>Dear sir,</p>
      <p>Sustainability is now a core part of every business plan. Companies of every size are asked to measure their impact, report it clearly and act on it. Our consultancy helps teams turn these goals into simple, concrete steps that fit daily work.</p>
      <p>In the first phase we review energy use, supply chains and waste, then we share a clear report with priorities and costs. Each action is planned with your staff, so that results can be tracked month by month and shared with clients and partners.</p>
      <p>We believe that a good plan is one that people can follow. For this reason every proposal is written in plain language and built around the real needs of your company.</p>
      <p>We would be glad to meet you and discuss how we can support your next steps. Please find our contact details above.</p>
      <div class="sign-row">
        <p>Yours Sincerely,<br>Elio Varenna</p>
        <div class="signature" role="img" aria-label="Handwritten signature"></div>
      </div>
    </div>
    <svg class="stripe" width="398" height="6" viewBox="0 0 398 6" aria-hidden="true">
      <rect width="398" height="6" fill="var(--stripe-grey)"/>
      <polygon points="270,6 276,0 398,0 398,6" fill="var(--ink-blue)"/>
    </svg>
  </section>

  <!-- Folder -->
  <section class="piece blue-fill folder">
    <div class="spine"></div>
    <div class="brand light"><span class="dot"></span><span>pianoverde</span></div>
    <div class="site">www.pianoverde.it</div>
  </section>

  <!-- Business card, side B -->
  <section class="piece paper card-front">
    <div class="holder">
      <div class="name">LUCA FERENTINO</div>
      <div class="role">Co-fondatore</div>
    </div>
    <div class="brand"><span class="dot"></span><span>pianoverde</span></div>
    <ul class="card-contacts">
      <li><svg viewBox="0 0 10 10"><rect x="3" y="0" width="4" height="10" rx="1"/></svg>+39 348 915 2074</li>
      <li><svg viewBox="0 0 10 10"><path d="M2 0h2l1 3-1.5 1a6 6 0 0 0 2.5 2.5L7 5l3 1v2l-1 2A9 9 0 0 1 0 1z"/></svg>+39 348 915 2070</li>
      <li><svg viewBox="0 0 10 10"><rect x="0" y="2" width="10" height="6"/></svg>luca@pianoverde.it</li>
      <li><svg viewBox="0 0 10 10"><circle cx="5" cy="5" r="5"/></svg>www.pianoverde.it</li>
    </ul>
    <div class="card-company">
      <div class="company">PIANOVERDE SRL</div>
      <div>Via Lucerna, 7</div>
      <div>21047 - Saronno (VA)</div>
    </div>
    <svg class="stripe" width="171" height="3" viewBox="0 0 171 3" aria-hidden="true">
      <rect width="171" height="3" fill="var(--stripe-grey)"/>
      <polygon points="104,3 107,0 171,0 171,3" fill="var(--ink-blue)"/>
    </svg>
  </section>

  <!-- Business card, side A -->
  <section class="piece blue-fill card-back">
    <div class="brand light"><span class="dot"></span><span>pianoverde</span></div>
    <div class="site">www.pianoverde.it</div>
  </section>

  <!-- Compliment slip -->
  <section class="piece paper slip">
    <div class="brand"><span class="dot"></span><span>pianoverde</span></div>
    <div class="contact-block">
      <div class="company">PIANOVERDE SRL</div>
      <div>Via Lucerna, 7</div>
      <div>21047 - Saronno (VA)</div>
    </div>
    <svg class="stripe" width="415" height="6" viewBox="0 0 415 6" aria-hidden="true">
      <rect width="415" height="6" fill="var(--stripe-grey)"/>
      <polygon points="286,6 292,0 415,0 415,6" fill="var(--ink-blue)"/>
    </svg>
  </section>

  <!-- Envelope -->
  <section class="piece paper envelope">
    <svg class="flap" width="415" height="59" viewBox="0 0 415 59" aria-hidden="true">
      <polygon points="0,0 415,0 401,59 14,59" fill="var(--blue)"/>
    </svg>
    <div class="brand"><span class="dot"></span></div>
    <div class="site">www.pianoverde.it</div>
  </section>

</body>
</html>
```